Harborline Crest Insurance Services

we are a high end insurance agency we specialize on Auto | Home | Business | Life looking for something professional and luxuries at the same time. if you guys need anything else please let me know.

Auto | Home | Business | Life must be under logo on the back with black background.

i want the back part to be black with our gold logo on it.

Target Market(s)

Auto | Home | Business | Life

Industry/Entity Type

Insurance Broker

Contact Information for Business Card

My logo is gold so a black in the back would be nice.

Font styles to use
Serif

Colors
000000

Requirements
Must have
• Big logo on the back with black background.

```html
<!DOCTYPE html>
<html lang="en">
<head>
<meta charset="utf-8">
<title>Harborline Crest Insurance Services – Business Cards</title>
<link rel="stylesheet" href="https://fonts.googleapis.com/css2?family=Cinzel:wght@600&family=Libre+Baskerville&family=Open+Sans:wght@400;600&display=swap">
<style>
  :root {
    --backdrop: #1d1d1d;
    --card-white: #ffffff;
    --card-black: #000000;
    --brand-yellow: #fdb913;
    --brand-gold: #e0a91c;
    --ink-dark: #222222;
    --ink-grey: #6b6b6b;
    --ink-soft: #8c8c8c;
  }
  * { box-sizing: border-box; margin: 0; padding: 0; }
  html, body {
    width: 1200px; height: 1000px; overflow: hidden;
    background: var(--backdrop);
  }
  .stage { position: relative; width: 1200px; height: 1000px; }
  .card {
    position: absolute;
    width: 560px; height: 320px;
    border-radius: 26px;
    overflow: hidden;
    box-shadow: 0 18px 40px rgba(0,0,0,.55);
  }

  /* Logo side (black, gold name) */
  .card--logo { left: 100px; top: 110px; background: var(--card-black); }
  .logo__brand {
    position: absolute; left: 0; right: 0; top: 96px;
    display: flex; flex-direction: column; align-items: center; gap: 8px;
  }
  .logo__name {
    font-family: 'Cinzel', serif; font-weight: 600;
    font-size: 34px; line-height: 1.1; color: var(--brand-gold); letter-spacing: 1px;
    display: flex; align-items: center; gap: 12px;
  }
  .logo__dot { width: 16px; height: 16px; border-radius: 50%; background: var(--brand-gold); }
  .logo__sub {
    font-family: 'Cinzel', serif; font-weight: 600;
    font-size: 15px; color: var(--brand-gold); letter-spacing: 6px;
  }
  .logo__band {
    position: absolute; left: 0; right: 0; bottom: 0; height: 64px;
    background: var(--brand-yellow);
    display: flex; align-items: center; justify-content: center;
  }
  .logo__services {
    font-family: 'Libre Baskerville', serif;
    font-size: 17px; color: #fff; letter-spacing: 2.5px;
  }

  /* Contact side */
  .card--contact { left: 540px; top: 540px; background: var(--card-white); }
  .contact__panel {
    position: absolute; left: 0; top: 0; bottom: 0; width: 205px;
    background: var(--brand-yellow);
  }
  .contact__brand {
    position: absolute; left: 222px; top: 38px;
    font-family: 'Cinzel', serif; font-weight: 600;
    color: var(--ink-dark);
  }
  .contact__brand-name { font-size: 24px; letter-spacing: .5px; line-height: 1.15; }
  .contact__brand-sub { font-size: 11px; letter-spacing: 4px; }
  .contact__details {
    position: absolute; right: 34px; top: 128px;
    text-align: right;
    font-family: 'Open Sans', sans-serif; color: var(--ink-grey);
  }
  .contact__person {
    font-weight: 600; font-size: 21px; line-height: 1.3; color: var(--ink-dark); letter-spacing: .3px;
  }
  .contact__role {
    font-weight: 600; font-size: 11px; color: var(--ink-soft); letter-spacing: .5px; margin-bottom: 14px;
  }
  .contact__line {
    font-size: 13px; line-height: 19px;
    display: flex; justify-content: flex-end; align-items: center;
  }
  .contact__line--gap { margin-top: 10px; }
  .contact__text { white-space: nowrap; }
  .contact__icon {
    flex: 0 0 11px; width: 11px; height: 11px; margin-left: 9px;
    fill: var(--brand-yellow);
  }
  .contact__web-accent { color: var(--brand-yellow); }
</style>
</head>
<body>
<main class="stage">
  <section class="card card--logo" aria-label="Business card logo side">
    <div class="logo__brand">
      <div class="logo__name"><span class="logo__dot"></span>Harborline Crest</div>
      <div class="logo__sub">INSURANCE SERVICES</div>
    </div>
    <div class="logo__band">
      <p class="logo__services">AUTO | HOME | BUSINESS | LIFE</p>
    </div>
  </section>

  <section class="card card--contact" aria-label="Business card contact side">
    <div class="contact__panel"></div>
    <div class="contact__brand">
      <div class="contact__brand-name">Harborline Crest</div>
      <div class="contact__brand-sub">INSURANCE SERVICES</div>
    </div>
    <div class="contact__details">
      <div class="contact__person">ADRIAN HALE</div>
      <div class="contact__role">CEO &amp; FOUNDER</div>
      <div class="contact__line"><span class="contact__text">Your Street Address</span><span class="contact__icon"></span></div>
      <div class="contact__line"><span class="contact__text">Singapore, 1234</span><span class="contact__icon"></span></div>
      <div class="contact__line contact__line--gap">
        <span class="contact__text">+000 12345 6789</span>
        <svg class="contact__icon" viewBox="0 0 24 24"><path d="M6.6 10.8a15 15 0 0 0 6.6 6.6l2.2-2.2a1 1 0 0 1 1-.25 11.4 11.4 0 0 0 3.6.6 1 1 0 0 1 1 1V20a1 1 0 0 1-1 1A17 17 0 0 1 3 4a1 1 0 0 1 1-1h3.5a1 1 0 0 1 1 1c0 1.25.2 2.45.6 3.6a1 1 0 0 1-.25 1z"/></svg>
      </div>
      <div class="contact__line">
        <span class="contact__text">name@harborcrest.net</span>
        <svg class="contact__icon" viewBox="0 0 24 24"><path d="M2 5h20v14H2z"/><path d="M2 5l10 8 10-8" fill="none" stroke="#fff" stroke-width="1.8"/></svg>
      </div>
      <div class="contact__line">
        <span class="contact__text">www.<span class="contact__web-accent">harborcrestins</span>.net</span>
        <svg class="contact__icon" viewBox="0 0 24 24"><circle cx="12" cy="12" r="10"/><path d="M2 12h20M12 2c3 3 3 17 0 20M12 2c-3 3-3 17 0 20" fill="none" stroke="#fff" stroke-width="1.5"/></svg>
      </div>
    </div>
  </section>
</main>
</body>
</html>
```